Healthy lifestyle Influencer business card

I need your creativity to have a business card that I can leave in all the restaurants, hotels and spas I visit to inform them that I am an influencer specializing in the wellness sector and that I will write a review about them. You can use my instagram photos Velusport72 or on my website www.piattileggerinuovi.it. I would like my business card to impress with its creativity! thank you very much!

Contact Information for Business Card

siteweb, instagram, phone number

Font styles to use
Decorative
Script

Colors
0094D4
00A9DD
6FCCEA
C7EBF8
E9F6FB
59FF00
82FF00
B8FF75
E3FFCB
F4FFEA
FFC000
F8CF3A
FAE287
FDF2CF
FEFAEE
F0912C
F2A743
F7CA91
FBE8D2
FDF5EE
EE7325
F08F49
F5BC92
FAE3D3
FDF4ED
EB3D1F
EC4F4E
F09395
F8D3D4
FCEDEE
E54698
E96AAD
F1A4CE
F9D9EA
FCEFF6

Requirements
Nice to have
• creativity

```html
<!DOCTYPE html>
<html lang="it">
<head>
<meta charset="utf-8">
<title>Vela Cucina Sana – biglietto da visita</title>
<link rel="stylesheet" href="https://fonts.googleapis.com/css2?family=Pinyon+Script&family=Quicksand:wght@500&family=Roboto:wght@300;400&display=swap">
<style>
  :root {
    --stage: #2d2d2d;
    --teal-top: #86afa4;
    --teal-bottom: #97bcb1;
    --paper: #f1f1f0;
    --paper-shade: #e6e6e5;
    --ink: #3a3a3a;
    --ink-soft: #4a4a4a;
    --icon: #8fb3a9;
    --band-dark: #474747;
    --band-teal: #8fb5aa;
    --band-text: #e8e8e8;
  }
  * { margin: 0; padding: 0; box-sizing: border-box; }
  html, body { width: 1200px; height: 1138px; overflow: hidden; }
  body { background: var(--stage); position: relative; font-family: "Roboto", sans-serif; }

  .card { position: absolute; width: 621px; height: 375px; border-radius: 16px; overflow: hidden; }
  .card--front { left: 272px; top: 184px; background: linear-gradient(180deg, var(--teal-top), var(--teal-bottom)); }
  .card--back { left: 274px; top: 606px; background: linear-gradient(180deg, var(--paper), var(--paper-shade)); }

  .photo-grid { position: absolute; left: 24px; top: 22px; display: grid;
    grid-template-columns: repeat(3, 185px); grid-template-rows: repeat(2, 104px); gap: 9px 10px; }
  .photo { border-radius: 2px; }
  .photo--mousse { background: linear-gradient(135deg, #efeded, #b59a92); }
  .photo--redvelvet { background: linear-gradient(135deg, #d9c3b8, #b04a45); }
  .photo--berrycup { background: linear-gradient(135deg, #6b5a45, #3c4f86); }
  .photo--blueberrytart { background: linear-gradient(135deg, #3f4654, #e3d9dc); }
  .photo--cheesecake { background: linear-gradient(135deg, #c98a55, #7a4a25); }
  .photo--coconut { background: linear-gradient(135deg, #f2ebe2, #d7b07a); }

  .brand { position: absolute; text-align: center; color: var(--ink);
    font-family: "Quicksand", sans-serif; font-weight: 500; }
  .brand__name { line-height: 1; white-space: nowrap; }
  .brand__tagline { white-space: nowrap; }

  .card--front .brand { left: 0; right: 0; top: 284px; }
  .card--front .brand__name { font-size: 28px; }
  .card--front .brand__tagline { font-size: 13px; margin-top: 14px; }

  .card--back .brand { left: 20px; width: 310px; top: 160px; }
  .card--back .brand__name { font-size: 30px; }
  .card--back .brand__tagline { font-size: 14px; margin-top: 14px; }

  .owner { position: absolute; left: 360px; top: 106px; font-family: "Pinyon Script", cursive;
    font-size: 30px; color: var(--ink); }
  .contact-list { position: absolute; left: 366px; top: 154px; list-style: none; }
  .contact-list li { display: flex; align-items: center; height: 24px;
    font-size: 16px; font-weight: 300; color: var(--ink-soft); }
  .contact-list svg { width: 14px; height: 14px; margin-right: 12px; fill: var(--icon); }
  .vat { position: absolute; left: 369px; top: 234px; font-size: 16px; font-weight: 300; color: var(--ink-soft); }

  .band { position: absolute; left: 0; bottom: 0; width: 621px; height: 47px; }
  .social { position: absolute; left: 398px; top: 340px; display: flex; align-items: center;
    font-size: 16px; font-weight: 300; color: var(--band-text); }
  .social__dot { width: 12px; height: 12px; border-radius: 50%; background: var(--band-teal); margin-right: 12px; }
</style>
</head>
<body>

<section class="card card--front" aria-label="Fronte del biglietto">
  <div class="photo-grid">
    <div class="photo photo--mousse" role="img" aria-label="Foto di mousse al cioccolato in ciotola di vetro"></div>
    <div class="photo photo--redvelvet" role="img" aria-label="Foto di torta red velvet tagliata"></div>
    <div class="photo photo--berrycup" role="img" aria-label="Foto di coppa con frutti di bosco"></div>
    <div class="photo photo--blueberrytart" role="img" aria-label="Foto di crostata ai mirtilli"></div>
    <div class="photo photo--cheesecake" role="img" aria-label="Foto di cheesecake in tortiera"></div>
    <div class="photo photo--coconut" role="img" aria-label="Foto di biscotti al cocco"></div>
  </div>
  <div class="brand">
    <div class="brand__name">Vela Cucina Sana</div>
    <div class="brand__tagline">Leggeri con gusto, ogni giorno</div>
  </div>
</section>

<section class="card card--back" aria-label="Retro del biglietto">
  <div class="brand">
    <div class="brand__name">Vela Cucina Sana</div>
    <div class="brand__tagline">Leggeri con gusto, ogni giorno</div>
  </div>

  <div class="owner">Vela Rinaldi</div>
  <ul class="contact-list">
    <li><svg viewBox="0 0 16 16"><path d="M2 6c0-2 3-3 6-3s6 1 6 3v1h-3V6H5v1H2zM4 8h8l1 5H3z"/></svg>000-0000-0000</li>
    <li><svg viewBox="0 0 16 16"><path d="M1 3h14v10H1zM2.5 4.5 8 9l5.5-4.5v7h-11z" fill-rule="evenodd"/></svg>info@piattileggerinuovi.it</li>
    <li><svg viewBox="0 0 16 16"><path d="M8 1a7 7 0 1 0 0 14A7 7 0 0 0 8 1zm0 1.5c.8.9 1.5 2.5 1.7 4.5H6.3C6.5 5 7.2 3.4 8 2.5zM5 7H2.6A5.5 5.5 0 0 1 6 2.8C5.5 4 5.1 5.4 5 7zm6 0c-.1-1.6-.5-3-1-4.2A5.5 5.5 0 0 1 13.4 7zM2.6 9H5c.1 1.6.5 3 1 4.2A5.5 5.5 0 0 1 2.6 9zm3.7 0h3.4c-.2 2-.9 3.6-1.7 4.5-.8-.9-1.5-2.5-1.7-4.5zM11 9h2.4a5.5 5.5 0 0 1-3.4 4.2c.5-1.2.9-2.6 1-4.2z"/></svg>www.piattileggerinuovi.it</li>
  </ul>
  <div class="vat">Partita IVA 05120390417</div>

  <svg class="band" viewBox="0 0 621 47" aria-hidden="true">
    <rect x="0" y="32" width="621" height="15" fill="var(--band-teal)"/>
    <path d="M294 0H621V47H262Z" fill="var(--band-dark)"/>
  </svg>
  <div class="social"><span class="social__dot"></span>@Velusport72</div>
</section>

</body>
</html>
```